Harborview Wellness Counseling
7 business cards, letterhead, envlp, fax cover
Harborview Wellness Counseling -
Creative Brief
Professional
Martin Oakridge
Owner/Manager
2875 Pellham Ridge Blvd. Suite 204 O'Fallon, MO 63412
oakridgehome@brisknet-mail.net
I need cards for each of my seven therapists. I will upload word file with their names and info. Letterhead should not use therapists names.

```html
<!DOCTYPE html>
<html lang="en">
<head>
<meta charset="utf-8">
<title>Harborview Wellness Counseling – Business Card</title>
<link rel="stylesheet" href="https://fonts.googleapis.com/css2?family=Arimo:wght@400;700&display=swap">
<style>
  :root {
    --paper: #ffffff;
    --ink: #1a1a1a;
    --brand-navy: #1f3b6f;
    --brand-orange: #f2a51f;
    --accent-red: #d8332b;
  }
  html, body {
    margin: 0;
    padding: 0;
    width: 1200px;
    height: 686px;
    overflow: hidden;
    background: var(--paper);
  }
  .card {
    position: relative;
    width: 1200px;
    height: 686px;
    background: var(--paper);
    font-family: "Arimo", Arial, sans-serif;
    color: var(--ink);
  }
  .brand {
    position: absolute;
    left: 250px;
    top: 96px;
    display: flex;
    align-items: center;
    gap: 26px;
  }
  .brand-dot {
    width: 70px;
    height: 70px;
    border-radius: 50%;
    background: var(--brand-orange);
    flex: none;
  }
  .brand-name {
    font-size: 46px;
    font-weight: 700;
    color: var(--brand-navy);
    letter-spacing: 0.5px;
    white-space: nowrap;
  }
  .person {
    position: absolute;
    left: 0;
    width: 1200px;
    top: 370px;
    text-align: center;
  }
  .person-name {
    font-size: 29px;
    font-weight: 700;
    margin: 0;
    line-height: 1.35;
  }
  .person-role {
    font-size: 28px;
    margin: 0;
    line-height: 1.35;
  }
  .address {
    position: absolute;
    left: 43px;
    top: 502px;
    font-size: 27px;
    line-height: 43px;
    margin: 0;
    font-style: normal;
  }
  .email {
    position: absolute;
    left: 43px;
    top: 608px;
    font-size: 27px;
    margin: 0;
  }
  .phones {
    position: absolute;
    left: 912px;
    top: 576px;
    font-size: 27px;
    line-height: 41px;
    margin: 0;
  }
  .phones .label {
    display: inline-block;
    width: 80px;
  }
  .accent-band {
    position: absolute;
    left: 0;
    bottom: 0;
    width: 1200px;
    height: 19px;
    background: var(--accent-red);
  }
</style>
</head>
<body>
  <div class="card">
    <div class="brand">
      <span class="brand-dot"></span>
      <span class="brand-name">Harborview Wellness Counseling</span>
    </div>

    <div class="person">
      <p class="person-name">Martin Oakridge</p>
      <p class="person-role">Owner/Manager</p>
    </div>

    <address class="address">2875 Pellham Ridge Blvd.,<br>Suite 204, O'Fallon, MO 63412</address>
    <p class="email">oakridgehome@brisknet-mail.net</p>

    <p class="phones">
      <span class="label">Ph:</span> 636-555-0147<br>
      <span class="label">Fax:</span>636-555-0192
    </p>

    <div class="accent-band"></div>
  </div>
</body>
</html>
```